'Shires at Roundtable'

We are after a flyer to sell a two day conference to sponsors, delegates and other Councils to participate.
The conference aims to be a forum for Northern Territory Councils to get together and discuss ideas, issues and overcome challenges and isolation in collaboration.
The conference will be a inaugural event with the plan to host a annual two day conference each year with a specific theme relevant to all Northern Territory Councils. - Give the Councils a voice.

```html
<!DOCTYPE html>
<html lang="en">
<head>
<meta charset="utf-8">
<title>Shires at Roundtable – Two Day Conference</title>
<link rel="stylesheet" href="https://fonts.googleapis.com/css2?family=Syncopate&family=Arimo:ital,wght@0,400;1,700&display=swap">
<style>
  :root {
    --bg-light: #e9e7e4;
    --bg-mid: #cfcac3;
    --bg-dark: #a8a097;
    --grid-line: rgba(255,255,255,0.35);
    --band: #2b2b2b;
    --ink: #111111;
    --white: #ffffff;
    --blue-deep: #0a5f9e;
    --blue-bright: #1a86c8;
    --blue-pale: #9fc6e4;
    --sky: #b9d3ea;
    --sea: #6f8d9c;
    --tile-pink: rgba(226,150,160,0.6);
    --tile-orange: rgba(230,160,120,0.6);
    --tile-yellow: rgba(236,220,110,0.6);
    --tile-green: rgba(200,210,150,0.45);
    --tile-red: rgba(210,110,120,0.55);
    --tile-tan: rgba(236,200,140,0.5);
    --tile-blue: rgba(170,210,225,0.5);
  }
  html, body { margin: 0; padding: 0; overflow: hidden; }
  body { width: 849px; height: 1200px; background: var(--bg-light); }
  .flyer {
    position: relative; width: 849px; height: 1200px; overflow: hidden;
    background:
      repeating-linear-gradient(90deg, transparent 0 113px, var(--grid-line) 113px 115px),
      repeating-linear-gradient(0deg, transparent 0 113px, var(--grid-line) 113px 115px),
      radial-gradient(ellipse at 70% 55%, var(--bg-light) 0%, var(--bg-mid) 55%, var(--bg-dark) 100%);
  }
  .layer { position: absolute; left: 0; top: 0; }
  .title {
    position: absolute; left: 60px; top: 92px; margin: 0;
    font-family: "Syncopate", sans-serif; font-weight: 400;
    font-size: 60px; line-height: 64px; letter-spacing: 1px;
    color: var(--white); text-transform: uppercase;
  }
  .date-band {
    position: absolute; left: 0; top: 238px; width: 849px; height: 46px;
    background: var(--band);
  }
  .date {
    position: absolute; right: 76px; top: 240px; margin: 0;
    font-family: "Arimo", sans-serif; font-size: 35px; letter-spacing: 1px;
    color: var(--white);
  }
  .details {
    position: absolute; left: 380px; top: 294px; width: 420px;
    font-family: "Arimo", sans-serif; font-style: italic; font-weight: 700;
    color: var(--ink); text-transform: uppercase;
  }
  .details h2 { margin: 0; font-size: 30px; line-height: 36px; }
  .details p { margin: 4px 0 0; font-size: 14.5px; line-height: 14px; }
  .details p + p { margin-top: 24px; }
  .details .audience { margin-top: 4px; }
  .tiles {
    position: absolute; left: 418px; top: 566px;
    display: grid; grid-template-columns: repeat(3, 103px); grid-auto-rows: 103px; gap: 16px 13px;
  }
  .tile { border-radius: 14px; }
  .tile.pink { background: var(--tile-pink); }
  .tile.orange { background: var(--tile-orange); }
  .tile.yellow { background: var(--tile-yellow); }
  .tile.green { background: var(--tile-green); }
  .tile.red { background: var(--tile-red); }
  .tile.tan { background: var(--tile-tan); }
  .tile.blue { background: var(--tile-blue); grid-column: 3; }
  .council-name {
    position: absolute; left: 82px; top: 745px; width: 170px; margin: 0;
    font-family: "Arimo", sans-serif; font-size: 22px; line-height: 26px;
    color: var(--band); text-align: center;
  }
</style>
</head>
<body>
<main class="flyer">
  <svg class="layer backdrop" width="849" height="1200" viewBox="0 0 849 1200" aria-hidden="true">
    <defs>
      <linearGradient id="blueFade" x1="0" y1="0" x2="0" y2="1">
        <stop offset="0" stop-color="#1a86c8"/>
        <stop offset="1" stop-color="#0a4f86"/>
      </linearGradient>
    </defs>
    <rect x="-200" y="900" width="560" height="500" fill="url(#blueFade)"/>
    <rect x="420" y="920" width="452" height="452" rx="22" transform="rotate(45 645 1146)" fill="url(#blueFade)"/>
    <rect x="230" y="1160" width="90" height="90" rx="12" transform="rotate(45 275 1205)" fill="#333"/>
  </svg>

  <svg class="layer water-panel" width="849" height="1200" viewBox="0 0 849 1200" role="img" aria-label="Textured blue water photograph">
    <defs>
      <linearGradient id="water" x1="0" y1="0" x2="1" y2="1">
        <stop offset="0" stop-color="#9fc6e4"/>
        <stop offset="0.5" stop-color="#3f86c0"/>
        <stop offset="1" stop-color="#1b5f9c"/>
      </linearGradient>
    </defs>
    <rect x="-172" y="298" width="335" height="335" rx="20" transform="rotate(45 -5 465)" fill="url(#water)"/>
  </svg>

  <svg class="layer beach-panel" width="849" height="1200" viewBox="0 0 849 1200" role="img" aria-label="Photograph of a calm sea beneath a pale sky">
    <defs>
      <linearGradient id="seaSky" x1="0" y1="0" x2="0" y2="1">
        <stop offset="0" stop-color="#a9c8e6"/>
        <stop offset="0.55" stop-color="#dfe9f2"/>
        <stop offset="0.64" stop-color="#6f8d9c"/>
        <stop offset="0.78" stop-color="#c9d6dd"/>
        <stop offset="1" stop-color="#ffffff"/>
      </linearGradient>
    </defs>
    <rect x="68" y="578" width="424" height="424" rx="26" transform="rotate(45 280 790)" fill="url(#seaSky)" stroke="#3a3a3a" stroke-width="4"/>
  </svg>

  <h1 class="title">Shires at<br>Roundtable</h1>
  <div class="date-band"></div>
  <p class="date">13th-14th April 2011</p>

  <section class="details">
    <h2>Two Day Conference</h2>
    <p class="audience">To sponsors, delegates and other councils<br>to participate.</p>
    <p>A forum for Northern Territory<br>councils to get together and<br>discuss ideas issues and overcome<br>challenges and isolation<br>in collaboration.</p>
    <p>Conference will be for all<br>Northern Territory councils<br>- giving councils a voice.</p>
  </section>

  <div class="tiles" aria-hidden="true">
    <div class="tile pink"></div><div class="tile orange"></div><div class="tile yellow"></div>
    <div class="tile green"></div><div class="tile red"></div><div class="tile tan"></div>
    <div class="tile blue"></div>
  </div>

  <p class="council-name">Coral Bay Shire Council</p>
</main>
</body>
</html>
```